NEW Modern Sleek Business Card for VR Language Startup

Our startup is using VR to lead the next wave of world language education. We need a two-sided business card that introduces the larger organization (Quorvel Language Inc) and our contact info on one side and shows the product, Lumidrasca, on the other side.

Side 1 (contact info)= Quorvel Logo and Contact info (name, title, phone, email)

Side 2 (product)= Lumidrasc logo, text, and website
Text= Culturally Immersive Language Learning Games
Website= www.lumidrasc.example

Target Market(s)

Education, Technology

Contact Information for Business Card

Contact info will be updated upon approval of the design. For now, put this as a placeholder.

Perry Hollins
Founder & CEO
phollins@mailtrove.example
(555)-014-2736

Font styles to use
Other font styles liked:
• Gibson and Century Gothic are the brand fonts

Requirements
Nice to have
• I would love to see cohesion between the design and colors of the two logos. I have attached a few business card designs that I like, so you can get a feel for my preferred style.

```html
<!DOCTYPE html>
<html lang="en">
<head>
<meta charset="utf-8">
<title>Quorvel Language – Business Card</title>
<link rel="stylesheet" href="https://fonts.googleapis.com/css2?family=Montserrat:wght@300;400;600;700&display=swap">
<style>
  :root {
    --stage: #3a3b3e;
    --card-dark: #1b1b1d;
    --card-dark-2: #262629;
    --blue-deep: #0a5aa3;
    --blue-mid: #0b71c2;
    --blue-bright: #0d9be3;
    --band: #0b0b0c;
    --white: #ffffff;
    --muted: #505053;
    --accent: #3a8fe0;
    --brand-font: "Montserrat", sans-serif;
  }
  * { box-sizing: border-box; margin: 0; padding: 0; }
  html, body {
    width: 1200px; height: 900px; overflow: hidden;
    background: var(--stage);
    font-family: var(--brand-font);
  }
  .canvas {
    position: relative; width: 1200px; height: 900px;
  }
  .card {
    position: absolute; left: 250px; width: 700px; height: 400px;
    border-radius: 28px; overflow: hidden;
    background: linear-gradient(135deg, var(--card-dark-2), var(--card-dark));
  }
  .card--contact { top: 40px; }
  .card--product { top: 470px; }

  /* Contact side */
  .contact-layers { position: absolute; inset: 0; }
  .org-mark {
    position: absolute; left: 48px; top: 150px;
    display: flex; align-items: center; gap: 18px;
    color: var(--white); font-weight: 600;
  }
  .org-mark__dot {
    width: 58px; height: 58px; border-radius: 50%;
    background: var(--accent);
  }
  .org-mark__name { line-height: 1.15; }
  .org-mark__line1 { display: block; font-size: 34px; letter-spacing: 6px; }
  .org-mark__line2 { display: block; font-size: 15px; letter-spacing: 9px; }

  .person {
    position: absolute; right: 40px; top: 98px; text-align: right;
    color: var(--white);
  }
  .person__name { font-size: 28px; font-weight: 700; letter-spacing: 1px; }
  .person__title { font-size: 15px; font-weight: 400; letter-spacing: 1.5px; margin-top: 2px; }

  .contact-list {
    position: absolute; right: 34px; top: 250px; list-style: none;
    color: var(--white);
  }
  .contact-list li {
    display: flex; justify-content: flex-end; align-items: baseline; gap: 14px;
    font-size: 17px; font-weight: 300; letter-spacing: 0.5px; margin-bottom: 8px;
  }
  .contact-list .label { font-weight: 700; font-size: 17px; width: 14px; text-align: center; }

  /* Product side */
  .product-mark {
    position: absolute; left: 0; right: 0; top: 80px;
    display: flex; flex-direction: column; align-items: center; gap: 20px;
  }
  .product-mark__dot {
    width: 120px; height: 120px; border-radius: 50%;
    background: var(--accent);
  }
  .product-mark__name {
    color: var(--white); font-size: 56px; font-weight: 600; letter-spacing: 0.5px;
  }
  .tagline {
    position: absolute; left: 0; right: 0; top: 300px; text-align: center;
    color: var(--muted); font-size: 17px; letter-spacing: 1.5px; text-transform: uppercase;
  }
  .website {
    position: absolute; left: 0; right: 0; top: 332px; text-align: center;
    color: var(--white); font-size: 20px; letter-spacing: 1px; text-transform: uppercase;
  }
</style>
</head>
<body>
<main class="canvas">

  <section class="card card--contact" aria-label="Contact side">
    <svg class="contact-layers" width="700" height="400" viewBox="0 0 700 400" aria-hidden="true">
      <polygon points="330,0 700,0 700,400 400,400" fill="var(--blue-deep)"/>
      <polygon points="360,0 700,0 700,400 430,400" fill="var(--blue-mid)"/>
      <polygon points="390,0 700,0 700,400 470,400" fill="var(--blue-bright)"/>
      <rect x="340" y="92" width="360" height="74" fill="var(--band)"/>
      <rect x="300" y="166" width="70" height="38" fill="var(--band)"/>
    </svg>

    <div class="org-mark">
      <span class="org-mark__dot"></span>
      <span class="org-mark__name">
        <span class="org-mark__line1">QUORVEL</span>
        <span class="org-mark__line2">LANGUAGE</span>
      </span>
    </div>

    <div class="person">
      <p class="person__name">PERRY HOLLINS</p>
      <p class="person__title">FOUNDER &amp; CEO</p>
    </div>

    <ul class="contact-list">
      <li><span>PHOLLINS@MAILTROVE.EXAMPLE</span><span class="label">E</span></li>
      <li><span>(555)-014-2736</span><span class="label">P</span></li>
    </ul>
  </section>

  <section class="card card--product" aria-label="Product side">
    <div class="product-mark">
      <span class="product-mark__dot"></span>
      <span class="product-mark__name">Lumidrasc</span>
    </div>
    <p class="tagline">Culturally Immersive Language Learning Games</p>
    <p class="website">www.lumidrasc.example</p>
  </section>

</main>
</body>
</html>
```